VELINTA Promotions - Business Card Design Project

We are looking for a classy business cards for Promotion Company based in Toronto, Canada named Velinta Promotions.

Velinta Promotions has an idea and vision to set high standard, be EXCLUSIVE and attract a group of people that will follow us through events we promote (night clubs, brand promotions, music events, and sport events)

We want to present a high standards and classy image to the others...
Updates

Target Market(s)

male/female age 25-40 Target: business owners young entrepreneur - clubing industry - media industry - promotion industry - marketing media industry

Industry/Entity Type

Events

Requirements
Must have
• business cards should be classy, make people feel exclusive , make people react ..

```html
<!DOCTYPE html>
<html lang="en">
<head>
<meta charset="utf-8">
<title>Velinta Promotions – Business Card</title>
<link rel="stylesheet" href="https://fonts.googleapis.com/css2?family=Marcellus+SC&display=swap">
<style>
  :root {
    --stage: #141414;
    --maroon-light: #b23a6a;
    --maroon: #7a1236;
    --maroon-dark: #3a0818;
    --plum: #6a2a66;
    --violet: #4b3468;
    --cyan: #3fc6ee;
    --ink: #f4f0f6;
    --band: rgba(255, 255, 255, 0.16);
    --card-font: "Marcellus SC", "Copperplate", serif;
  }
  * { box-sizing: border-box; margin: 0; padding: 0; }
  html, body {
    width: 1200px;
    height: 871px;
    overflow: hidden;
    background: var(--stage);
    font-family: var(--card-font);
  }
  .canvas {
    position: relative;
    width: 1200px;
    height: 871px;
  }
  .card {
    position: absolute;
    left: 280px;
    width: 640px;
    height: 366px;
    border-radius: 4px;
    overflow: hidden;
    box-shadow: 0 12px 30px rgba(0, 0, 0, 0.6);
  }

  /* Front side */
  .card--front {
    top: 48px;
    background:
      radial-gradient(ellipse 55% 70% at 22% 40%, rgba(230, 130, 170, 0.55), transparent 70%),
      linear-gradient(115deg, var(--maroon-light) 0%, var(--maroon) 45%, var(--maroon-dark) 100%);
  }
  .card--front .brand {
    position: absolute;
    left: 0; right: 0; top: 160px;
    display: flex;
    justify-content: center;
    align-items: center;
    gap: 14px;
  }
  .brand-dot {
    width: 14px;
    height: 14px;
    border-radius: 50%;
    background: var(--cyan);
  }
  .brand-name {
    color: var(--cyan);
    font-size: 40px;
    letter-spacing: 2px;
    line-height: 1;
  }

  /* Back side */
  .card--back {
    top: 457px;
    background:
      radial-gradient(ellipse 60% 60% at 95% 10%, rgba(80, 110, 160, 0.55), transparent 70%),
      linear-gradient(160deg, var(--violet) 0%, var(--plum) 55%, #5a2050 100%);
  }
  .card--back .texture {
    position: absolute;
    inset: 0;
    background: radial-gradient(ellipse 70% 80% at 30% 70%, rgba(150, 60, 130, 0.35), transparent 70%);
  }
  .name-band {
    position: absolute;
    left: 0; top: 48px;
    width: 300px;
    height: 62px;
    background: var(--band);
  }
  .person {
    position: absolute;
    left: 70px; top: 52px;
    color: var(--ink);
    font-size: 20px;
    line-height: 27px;
    letter-spacing: 1px;
  }
  .card--back .brand {
    position: absolute;
    right: 36px; top: 54px;
    display: flex;
    align-items: center;
    gap: 8px;
  }
  .card--back .brand-dot { width: 9px; height: 9px; }
  .card--back .brand-name { font-size: 22px; letter-spacing: 1px; }

  .contact {
    position: absolute;
    left: 0; right: 0; top: 186px;
    list-style: none;
  }
  .contact li {
    position: relative;
    height: 28px;
    padding-left: 300px;
    color: var(--ink);
    font-size: 16px;
    line-height: 28px;
    letter-spacing: 1px;
    white-space: nowrap;
  }
  .contact li::before {
    content: "";
    position: absolute;
    left: 290px; right: 0; top: 3px;
    height: 23px;
    background: var(--band);
  }
  .contact span { position: relative; }
</style>
</head>
<body>
<main class="canvas">
  <section class="card card--front" aria-label="Front of card">
    <div class="brand">
      <span class="brand-dot"></span>
      <span class="brand-name">VELINTA Promotions</span>
    </div>
  </section>

  <section class="card card--back" aria-label="Back of card">
    <div class="texture" role="img" aria-label="Distressed purple grunge texture"></div>
    <div class="name-band"></div>
    <p class="person">Name<br>Proffesion</p>
    <div class="brand">
      <span class="brand-dot"></span>
      <span class="brand-name">VELINTA Promotions</span>
    </div>
    <ul class="contact">
      <li><span>Adress : Harbour Lane . 48213</span></li>
      <li><span>Telephone : 416.555.0182</span></li>
      <li><span>Mobile : 647.555.0139</span></li>
      <li><span>E-mail : name@velinta.com</span></li>
      <li><span>Web : www.velinta.com</span></li>
      <li><span>www.velinta.com</span></li>
    </ul>
  </section>
</main>
</body>
</html>
```